Parkinson's Disease Progression

Visually describe the rate of Parkinson progression in the first 15 years following diagnosis. Title: "Patient-Perceived Progression of Parkinsonism"

The attached figure names "meanqol" is the curve that should serve as the basis of this graphic. Everything else-- color, labels, font, etc. describe this curve.
Thank you!

Target Market(s)

People with Parkisnon's Disease, neurologists, family members.

Font styles to use
Sans Serif

Requirements
Must have
• Must have the lines going through these exact numbers
Excellent -- 502
Very good- 661
Good- 895
Fair- 1268
Poor- 1655

LABELS:
Title: "Patient-Perceived Progression of Parkinsonism"
"SAW-MX (Self-Assessed Wellbeing Index for Movement Conditions)" should be the label on the left.
"Quality of Life" should be the label on the right
"Years Since Diagnosis" should be the label on the bottom
Nice to have
• A color scheme that goes from GOOD (low numbers) to BAD (high numbers).

Easy to read (elderly)

```html
<!DOCTYPE html>
<html lang="en">
<head>
<meta charset="utf-8">
<title>Patient-Perceived Progression of Parkinsonism</title>
<link href="https://fonts.googleapis.com/css2?family=Oswald:wght@400;500;600;700&display=swap" rel="stylesheet">
<style>
  :root {
    --navy: #1e1d3d;
    --paper: #ffffff;
    --ink: #1a1a1a;
    --grid: #cfcfcf;
    --band: #c4c4c4;
    --axis-red: #b0243a;
    --muted: #9a9a9a;
    --excellent: #2f7d1f;
    --very-good: #84c155;
    --good: #e87b5c;
    --fair: #b22433;
    --poor: #6e2631;
  }
  html, body {
    margin: 0;
    padding: 0;
    width: 1200px;
    height: 820px;
    overflow: hidden;
    background: var(--paper);
  }
  .chart-card {
    position: relative;
    width: 1200px;
    height: 820px;
    background: var(--paper);
    font-family: "Oswald", "Arial Narrow", sans-serif;
  }
  .title-band {
    height: 113px;
    background: var(--navy);
    display: flex;
    align-items: center;
    justify-content: center;
  }
  .title-band h1 {
    margin: 0;
    color: var(--paper);
    font-weight: 500;
    font-size: 52px;
    letter-spacing: 2.4px;
    line-height: 1;
  }
  .progression-chart {
    position: absolute;
    left: 0;
    top: 0;
    width: 1200px;
    height: 820px;
  }
  .axis-line { stroke: var(--ink); stroke-width: 1.4; fill: none; }
  .axis-dot { fill: var(--ink); }
  .tick { stroke: var(--ink); stroke-width: 1.4; }
  .tick-label { font-family: "Oswald", sans-serif; font-size: 30px; font-weight: 500; fill: var(--ink); }
  .grid-line { stroke: var(--grid); stroke-width: 1.3; stroke-dasharray: 6 4; fill: none; }
  .band-line { stroke: var(--band); stroke-width: 1.8; stroke-dasharray: 8 6; fill: none; }
  .mean-line { stroke: #4a4a4a; stroke-width: 2; fill: none; }
  .tag-text { font-family: "Oswald", sans-serif; font-weight: 700; font-size: 44px; fill: var(--paper); }
  .tag-excellent { fill: var(--excellent); }
  .tag-very-good { fill: var(--very-good); }
  .tag-good { fill: var(--good); }
  .tag-fair { fill: var(--fair); }
  .tag-poor { fill: var(--poor); }
  .tag-shadow { fill: #000; opacity: 0.16; }
  .axis-title { font-family: "Oswald", sans-serif; font-weight: 600; fill: var(--axis-red); }
  .axis-title-y { font-size: 32px; letter-spacing: 9px; }
  .axis-title-x { font-size: 38px; letter-spacing: 7px; }
  .side-title { font-family: "Oswald", sans-serif; font-weight: 500; font-size: 36px; letter-spacing: 9px; fill: var(--muted); }
</style>
</head>
<body>
<main class="chart-card">
  <header class="title-band">
    <h1>Patient-Perceived Progression of Parkinsonism</h1>
  </header>

  <svg class="progression-chart" viewBox="362 247 1317 900" xmlns="http://www.w3.org/2000/svg" aria-label="Line chart of SAW-MX score over years since diagnosis">
    <defs>
      <filter id="tag-blur" x="-20%" y="-100%" width="140%" height="300%">
        <feGaussianBlur stdDeviation="7"/>
      </filter>
    </defs>

    <!-- grid -->
    <g class="grid">
      <line class="grid-line" x1="577" y1="495" x2="1450" y2="495"/>
      <line class="grid-line" x1="577" y1="634" x2="1450" y2="634"/>
      <line class="grid-line" x1="577" y1="725" x2="1450" y2="725"/>
      <line class="grid-line" x1="577" y1="804" x2="1450" y2="804"/>
    </g>

    <!-- axes -->
    <g class="axes">
      <polyline class="axis-line" points="573,445 573,974 1450,974"/>
      <circle class="axis-dot" cx="573" cy="445" r="6"/>
      <circle class="axis-dot" cx="1450" cy="974" r="6"/>

      <line class="tick" x1="560" y1="520" x2="573" y2="520"/>
      <line class="tick" x1="560" y1="595" x2="573" y2="595"/>
      <line class="tick" x1="560" y1="679" x2="573" y2="679"/>
      <line class="tick" x1="560" y1="763" x2="573" y2="763"/>
      <line class="tick" x1="560" y1="847" x2="573" y2="847"/>
      <line class="tick" x1="560" y1="931" x2="573" y2="931"/>

      <text class="tick-label" x="548" y="532" text-anchor="end">1200</text>
      <text class="tick-label" x="548" y="607" text-anchor="end">1000</text>
      <text class="tick-label" x="548" y="691" text-anchor="end">800</text>
      <text class="tick-label" x="548" y="775" text-anchor="end">600</text>
      <text class="tick-label" x="548" y="859" text-anchor="end">400</text>
      <text class="tick-label" x="548" y="943" text-anchor="end">200</text>

      <line class="tick" x1="629" y1="974" x2="629" y2="987"/>
      <line class="tick" x1="860" y1="974" x2="860" y2="987"/>
      <line class="tick" x1="1096" y1="974" x2="1096" y2="987"/>
      <line class="tick" x1="1337" y1="974" x2="1337" y2="987"/>

      <text class="tick-label" x="629" y="1026" text-anchor="middle">0</text>
      <text class="tick-label" x="860" y="1026" text-anchor="middle">5</text>
      <text class="tick-label" x="1096" y="1026" text-anchor="middle">10</text>
      <text class="tick-label" x="1337" y="1026" text-anchor="middle">15</text>
    </g>

    <!-- confidence band and mean curve -->
    <g class="curves">
      <path class="band-line" d="M598,752 C650,740 700,715 760,690 C820,660 870,640 960,632 C1000,628 1030,618 1060,605 C1150,560 1250,510 1320,465 C1350,450 1380,437 1395,428"/>
      <path class="band-line" d="M598,855 C640,810 700,770 760,740 C820,700 870,670 960,665 C1000,660 1030,655 1060,640 C1150,590 1250,540 1350,528 C1400,527 1420,535 1437,538"/>
      <path class="mean-line" d="M645,775 C700,740 760,700 800,685 C840,665 860,655 920,652 C980,650 1010,645 1040,634 C1060,625 1080,615 1100,605 C1150,575 1200,545 1245,525 C1275,512 1300,502 1320,497 C1360,485 1400,473 1435,463"/>
    </g>

    <!-- quality tags -->
    <g class="tag-shadows" filter="url(#tag-blur)">
      <ellipse class="tag-shadow" cx="710" cy="842" rx="95" ry="8"/>
      <ellipse class="tag-shadow" cx="835" cy="762" rx="95" ry="8"/>
      <ellipse class="tag-shadow" cx="1143" cy="672" rx="95" ry="8"/>
      <ellipse class="tag-shadow" cx="1210" cy="533" rx="95" ry="8"/>
      <ellipse class="tag-shadow" cx="1500" cy="474" rx="95" ry="8"/>
    </g>

    <g class="tag tag-excellent">
      <path d="M610,776 H790 A28.5,28.5 0 0 1 790,833 H610 V818 L600,804 L610,790 Z"/>
      <text class="tag-text" x="626" y="822" textLength="166">EXCELLENT</text>
    </g>
    <g class="tag tag-very-good">
      <path d="M735,696 H915 A28.5,28.5 0 0 1 915,753 H735 V739 L725,725 L735,711 Z"/>
      <text class="tag-text" x="752" y="743" textLength="170">VERY GOOD</text>
    </g>
    <g class="tag tag-good">
      <path d="M1043,606 H1223 A28.5,28.5 0 0 1 1223,663 H1043 V648 L1032,634 L1043,620 Z"/>
      <text class="tag-text" x="1068" y="653" textLength="98">GOOD</text>
    </g>
    <g class="tag tag-fair">
      <path d="M1311,467 H1130 A28.5,28.5 0 0 0 1130,524 H1311 V509 L1322,495 L1311,481 Z"/>
      <text class="tag-text" x="1205" y="514" textLength="82">FAIR</text>
    </g>
    <g class="tag tag-poor">
      <path d="M1400,408 H1580 A28.5,28.5 0 0 1 1580,465 H1400 V450 L1390,436 L1400,422 Z"/>
      <text class="tag-text" x="1425" y="455" textLength="98">POOR</text>
    </g>

    <!-- axis titles -->
    <text class="axis-title axis-title-y" transform="translate(460,720) rotate(-90)" text-anchor="middle">SAW-MX</text>
    <text class="axis-title axis-title-x" x="980" y="1100" text-anchor="middle">Years Since Diagnosis</text>
    <text class="side-title" transform="translate(1504,714) rotate(90)" text-anchor="middle">Quality of Life</text>
  </svg>
</main>
</body>
</html>
```